Thank You For Shopping / Hair Care Tips

I need “Thank You For Shopping”
Post cards made for my hair business !
I added pictures of post cards that I really like . I also added my LunaVex Wigs logo for you guys to use

I want the backside of the flyer to have hair care tips !
I want people to have full directions on how to care for their wigs

Target Market(s)

Im marking to young woman to older middle aged woman
Ages 23-66 . I want my flyer to look mature And classy

Industry/Entity Type

Hair And Beauty

Font styles to use
Serif
Script

Colors
e34699
e34298
e34398

Requirements
Must have
• The flyer must have the Instagram logo with my Instagram name next to it @luna.vex.wigs__
• Also it must have my “Luna Vex Wigs” logo that I’ve uploaded in the pictures section .
• Flyer had to be two sides . One side “ thank you for shopping “ side two “hair care tips”
• My website must be on the flyer - www.lunavexwigs.example
• The flyer must match the colors of my logo
• All white . With the pink and glitter sliver you see on my logo
Nice to have
• Nice to have a glitter border
Should not have
• The flyer should not have different colors that don’t match my logo
• It shouldn’t be made without having my Instagram or website on the flyer

```html
<!DOCTYPE html>
<html lang="en">
<head>
<meta charset="utf-8">
<title>LunaVex Wigs — Thank You Card &amp; Hair Care Tips</title>
<link href="https://fonts.googleapis.com/css2?family=Yellowtail&family=Dancing+Script:wght@600&family=Lora&family=Montserrat:wght@400;700&display=swap" rel="stylesheet">
<style>
  :root{
    --pink:#e34699;
    --pink-soft:#f4bcd9;
    --pink-pale:#fbe3ef;
    --silver:#a8a8a8;
    --silver-light:#e4e4e4;
    --silver-dark:#7d7d7d;
    --ink:#151515;
    --paper:#ffffff;
    --stage:#2b3142;
    --panel-grey:#ececec;
  }
  html,body{margin:0;padding:0;}
  body{
    width:1200px;height:1044px;overflow:hidden;
    background:var(--stage);
    font-family:"Montserrat",sans-serif;
    position:relative;
  }
  .card{
    position:absolute;left:100px;width:1000px;height:480px;
    background:var(--paper);
    box-shadow:0 10px 30px rgba(0,0,0,.35);
    overflow:hidden;
  }
  .card--front{top:30px;}
  .card--back{top:534px;}
  .card__frame{
    position:absolute;inset:22px;
    border:5px solid var(--silver);
    border-image:repeating-linear-gradient(45deg,var(--silver-dark) 0 2px,var(--silver-light) 2px 4px,var(--silver) 4px 6px) 5;
    pointer-events:none;
  }

  /* front */
  .brand-name{
    position:absolute;left:70px;top:190px;margin:0;
    font-family:"Yellowtail",cursive;font-weight:400;font-size:60px;line-height:1;
    color:var(--pink);white-space:nowrap;
  }
  .thank-you{
    position:absolute;left:480px;top:40px;margin:0;
    font-family:"Yellowtail",cursive;font-weight:400;font-size:96px;line-height:1;
    color:var(--pink);white-space:nowrap;
  }
  .for-shopping{
    position:absolute;left:570px;top:180px;width:290px;height:80px;
    background:var(--panel-grey);
    clip-path:polygon(6% 0,100% 8%,94% 100%,0 88%);
    display:flex;align-items:center;justify-content:center;
    font-family:"Dancing Script",cursive;font-weight:600;font-size:38px;color:var(--ink);
    white-space:nowrap;
  }
  .ornament{position:absolute;border-radius:50%;
    background:linear-gradient(90deg,rgba(160,160,160,0),rgba(160,160,160,.45),rgba(160,160,160,0));}
  .ornament--left{left:500px;top:212px;width:64px;height:16px;}
  .ornament--right{left:866px;top:222px;width:64px;height:16px;}
  .handle{
    position:absolute;display:flex;align-items:center;gap:10px;
    font-family:"Lora",serif;font-size:24px;color:var(--ink);white-space:nowrap;
  }
  .handle__mark{width:18px;height:18px;border-radius:4px;background:var(--pink);flex:none;}
  .card--front .handle{left:640px;top:306px;}
  .band{
    position:absolute;left:40px;right:40px;top:366px;height:56px;
    background:linear-gradient(90deg,var(--pink-soft) 0%,var(--pink) 45%,var(--pink) 65%,var(--pink-pale) 100%);
    display:flex;align-items:center;justify-content:center;
  }
  .band__url{font-family:"Montserrat",sans-serif;font-size:24px;letter-spacing:5px;color:#fff;white-space:nowrap;}

  /* back */
  .tips-title{
    position:absolute;left:60px;top:34px;margin:0;
    font-family:"Yellowtail",cursive;font-weight:400;font-size:68px;line-height:1;
    color:var(--pink);white-space:nowrap;
  }
  .ornament--tips{left:380px;top:114px;width:110px;height:12px;
    background:linear-gradient(90deg,rgba(227,70,153,0),rgba(227,70,153,.45),rgba(227,70,153,0));}
  .tips{
    position:absolute;margin:0;padding:0;list-style:none;
    font-weight:700;font-size:14px;line-height:23px;color:var(--ink);text-transform:uppercase;
  }
  .tips li{display:flex;gap:6px;}
  .tips__num{color:var(--pink);min-width:26px;flex:none;}
  .tips--first{left:60px;top:135px;width:440px;}
  .tips--second{left:540px;top:44px;width:410px;}
  .divider{position:absolute;left:518px;top:44px;width:1px;height:290px;background:var(--silver-light);}
  .band--handle{
    position:absolute;left:530px;right:40px;top:342px;height:40px;background:var(--pink);
    display:flex;align-items:center;justify-content:center;
  }
  .band--handle .handle{position:static;color:#fff;font-size:22px;}
  .band--handle .handle__mark{background:#fff;}
  .band--site{
    position:absolute;left:40px;right:40px;top:398px;height:44px;background:var(--pink);
    display:flex;align-items:center;gap:12px;padding-left:40px;
    font-family:"Lora",serif;font-size:22px;color:#fff;letter-spacing:1px;white-space:nowrap;
  }
</style>
</head>
<body>

<section class="card card--front" aria-label="Thank you card, front">
  <div class="card__frame"></div>
  <p class="brand-name">LunaVex Wigs</p>
  <h1 class="thank-you">Thank You</h1>
  <div class="ornament ornament--left" role="img" aria-label="Leaf sprig ornament"></div>
  <div class="for-shopping">For Shopping</div>
  <div class="ornament ornament--right" role="img" aria-label="Leaf sprig ornament"></div>
  <div class="handle"><span class="handle__mark"></span>@luna.vex.wigs__</div>
  <div class="band"><span class="band__url">- www.lunavexwigs.example -</span></div>
</section>

<section class="card card--back" aria-label="Hair care tips, back">
  <div class="card__frame"></div>
  <h2 class="tips-title">Hair care tips</h2>
  <div class="ornament ornament--tips" role="img" aria-label="Pink leaf sprig ornament"></div>
  <ol class="tips tips--first">
    <li><span class="tips__num">1.</span>Wash with lukewarm water</li>
    <li><span class="tips__num">2.</span>Condition correctly</li>
    <li><span class="tips__num">3.</span>Concentrate shampoo on the scalp</li>
    <li><span class="tips__num">4.</span>Be extra thorough with rinsing</li>
    <li><span class="tips__num">5.</span>Don't dry off using a towel</li>
    <li><span class="tips__num">6.</span>Protect hair before heat styling</li>
    <li><span class="tips__num">7.</span>Blow-dry with a brush</li>
    <li><span class="tips__num">8.</span>Only straighten and curl dry hair</li>
    <li><span class="tips__num">9.</span>Switch up your part</li>
    <li><span class="tips__num">10.</span>Give strands a break from ponytails</li>
    <li><span class="tips__num">11.</span>Lock in your look with hairspray</li>
  </ol>
  <div class="divider"></div>
  <ol class="tips tips--second">
    <li><span class="tips__num">12.</span>Your scalp needs care, too</li>
    <li><span class="tips__num">13.</span>Sleep on a silk pillowcase</li>
    <li><span class="tips__num">14.</span>Use dry-shampoo when your hair needs a refresh</li>
    <li><span class="tips__num">15.</span>Deep condition regularly</li>
    <li><span class="tips__num">16.</span>Air dry when you can</li>
    <li><span class="tips__num">17.</span>Shield your strands from UV rays</li>
    <li><span class="tips__num">18.</span>Trim your split ends</li>
    <li><span class="tips__num">19.</span>Keep hair hydrated</li>
    <li><span class="tips__num">20.</span>Use a wide-tooth comb on wet hair</li>
    <li><span class="tips__num">21.</span>Keep your hot tools on low or medium setting</li>
  </ol>
  <div class="band--handle"><div class="handle"><span class="handle__mark"></span>@luna.vex.wigs__</div></div>
  <div class="band--site">
    <svg width="20" height="20" viewBox="0 0 20 20" aria-hidden="true"><g fill="none" stroke="#fff" stroke-width="1.6"><circle cx="10" cy="10" r="8"/><ellipse cx="10" cy="10" rx="3.5" ry="8"/><line x1="2" y1="10" x2="18" y2="10"/></g></svg>
    www.lunavexwigs.example
  </div>
</section>

</body>
</html>
```